New Business Card for Casual Beachfront Cafe

Quirky Beachfront Cafe at Moana, South Australia needs a DOUBLE SIDED business card to print on PrintHarbor.

Target Market(s)

Business Cards sit on the counter for Guests to take with them. Please view our website www.saltreefcafe.com.au to get a feel for the Cafe. You may also view our Instagram at @saltreefcafe

Industry/Entity Type

Cafe / Restaurant

Contact Information for Business Card

Information equivalent to: Breakfast, Lunch, Dinner, Coffee, Takeaway / 117 Parade Moana SA 5169 / Menu & Opening Hours: www.saltreefcafe.com.au / ph (08) 8461 9273

Requirements
Must have
• Information equivalent to: Breakfast, Lunch, Dinner, Coffee, Takeaway / 117 Parade Moana SA 5169 / Menu & Opening Hours: www.saltreefcafe.com.au / ph (08) 8461 9273
Nice to have
• Potentially some of our trademark colours (Cafe can be searched via Seekly)
Should not have
• Must NOT have image of the building. May have the logo provided on one side but not necessarily, depending on how you wish to design the card

```html
<!DOCTYPE html>
<html lang="en">
<head>
<meta charset="utf-8">
<title>Salt Reef Cafe – Business Card</title>
<link rel="stylesheet" href="https://fonts.googleapis.com/css2?family=Oswald:wght@600;700&family=Roboto+Condensed:wght@700&family=Roboto:wght@400;500;700&family=Jost:wght@700&display=swap">
<style>
  :root {
    --bg: #2b2b2b;
    --rust: #a84d12;
    --rust-dash: #b0471a;
    --paper: #e8e600;
    --rim: #f4f1e4;
    --navy: #1d3b84;
    --ink: #1e1e1e;
  }
  * { margin: 0; padding: 0; box-sizing: border-box; }
  html, body { width: 1138px; height: 1200px; overflow: hidden; }
  body { background: var(--bg); position: relative; font-family: "Roboto", sans-serif; }

  .card {
    position: absolute; top: 276px; width: 376px; height: 620px;
    background: var(--rust); border-radius: 14px; padding: 13px;
  }
  .card--front { left: 154px; }
  .card--back { left: 578px; }
  .card__rim { width: 100%; height: 100%; background: var(--rim); border-radius: 6px; padding: 3px; }
  .card__face {
    position: relative; width: 100%; height: 100%;
    background: var(--paper); border-radius: 4px;
  }
  .card__face::before {
    content: ""; position: absolute; inset: 7px;
    border: 2px dashed var(--rust-dash); border-radius: 2px;
  }

  .brand {
    position: absolute; left: 0; right: 0; top: 56px;
    text-align: center; color: var(--navy);
    font-family: "Oswald", sans-serif; font-weight: 700;
    line-height: 0.95; letter-spacing: 1px;
  }
  .brand__top { display: block; font-size: 46px; }
  .brand__bottom { display: block; font-size: 66px; }

  .services { position: absolute; left: 0; right: 0; top: 236px; }
  .tag { position: absolute; width: 118px; height: 72px; }
  .tag svg { position: absolute; inset: 0; }
  .tag span {
    position: absolute; left: 0; right: 0; top: 17px; text-align: center;
    font-family: "Oswald", sans-serif; font-weight: 600; font-size: 21px;
    color: var(--navy); letter-spacing: 0.2px;
  }
  .tag--breakfast { left: 53px; top: 0; }
  .tag--lunch { left: 181px; top: 0; }
  .tag--dinner { left: 53px; top: 92px; }
  .tag--coffee { left: 181px; top: 92px; }
  .tag--takeaway { left: 117px; top: 180px; }

  .web {
    position: absolute; left: 0; right: 0; text-align: center;
    font-size: 16px; color: var(--ink); line-height: 26px;
  }
  .card--front .web { top: 530px; }
  .card--back .web { top: 528px; }
  .web b { font-weight: 700; }

  .call {
    position: absolute; left: 0; right: 0; top: 282px; text-align: center;
    font-family: "Jost", sans-serif; font-weight: 700; font-size: 26px; color: var(--rust);
  }
  .call__mark { font-size: 20px; margin: 0 12px; vertical-align: 2px; }
  .phone {
    position: absolute; left: 0; right: 0; top: 322px; text-align: center;
    font-family: "Roboto Condensed", sans-serif; font-weight: 700; font-size: 44px;
    color: var(--navy); letter-spacing: -0.5px;
  }
  .pin { position: absolute; left: 162px; top: 408px; width: 38px; height: 48px; }
  .address {
    position: absolute; left: 0; right: 0; top: 464px; text-align: center;
    font-weight: 500; font-size: 16.5px; color: var(--ink);
  }
  .divider {
    position: absolute; left: 60px; right: 60px; top: 512px;
    height: 1px; background: var(--rust);
  }
</style>
</head>
<body>

<section class="card card--front">
  <div class="card__rim">
    <div class="card__face">
      <h1 class="brand"><span class="brand__top">SALT REEF</span><span class="brand__bottom">CAFE</span></h1>

      <svg width="0" height="0" style="position:absolute">
        <defs>
          <path id="tag-shape" d="M10,5 Q59,0 108,5 Q116,6 116,15 L116,40 Q116,47 109,50 L66,69 Q59,72 52,69 L9,50 Q2,47 2,40 L2,15 Q2,6 10,5 Z"/>
          <path id="tag-inner" d="M14,11 Q59,7 104,11 Q110,12 110,18 L110,38 Q110,43 105,45 L64,63 Q59,65 54,63 L13,45 Q8,43 8,38 L8,18 Q8,12 14,11 Z"/>
        </defs>
      </svg>

      <ul class="services" style="list-style:none">
        <li class="tag tag--breakfast"><svg viewBox="0 0 118 72"><use href="#tag-shape" fill="#e8e600" stroke="#a84d12" stroke-width="3"/><use href="#tag-inner" fill="none" stroke="#b0471a" stroke-width="1" stroke-dasharray="3 2"/></svg><span>BREAKFAST</span></li>
        <li class="tag tag--lunch"><svg viewBox="0 0 118 72"><use href="#tag-shape" fill="#e8e600" stroke="#a84d12" stroke-width="3"/><use href="#tag-inner" fill="none" stroke="#b0471a" stroke-width="1" stroke-dasharray="3 2"/></svg><span>LUNCH</span></li>
        <li class="tag tag--dinner"><svg viewBox="0 0 118 72"><use href="#tag-shape" fill="#e8e600" stroke="#a84d12" stroke-width="3"/><use href="#tag-inner" fill="none" stroke="#b0471a" stroke-width="1" stroke-dasharray="3 2"/></svg><span>DINNER</span></li>
        <li class="tag tag--coffee"><svg viewBox="0 0 118 72"><use href="#tag-shape" fill="#e8e600" stroke="#a84d12" stroke-width="3"/><use href="#tag-inner" fill="none" stroke="#b0471a" stroke-width="1" stroke-dasharray="3 2"/></svg><span>COFFEE</span></li>
        <li class="tag tag--takeaway"><svg viewBox="0 0 118 72"><use href="#tag-shape" fill="#e8e600" stroke="#a84d12" stroke-width="3"/><use href="#tag-inner" fill="none" stroke="#b0471a" stroke-width="1" stroke-dasharray="3 2"/></svg><span>TAKEAWAY</span></li>
      </ul>

      <p class="web">Menu &amp; Opening Hours<br>www.<b>saltreefcafe</b>.com.au</p>
    </div>
  </div>
</section>

<section class="card card--back">
  <div class="card__rim">
    <div class="card__face">
      <h2 class="brand"><span class="brand__top">SALT REEF</span><span class="brand__bottom">CAFE</span></h2>

      <p class="call"><span class="call__mark">&#8250;</span>Call Now<span class="call__mark">&#8249;</span></p>
      <p class="phone">(08) 8461 9273</p>

      <svg class="pin" viewBox="0 0 38 48" aria-hidden="true">
        <path d="M19,46 C19,46 3,28 3,18 A16,16 0 0 1 35,18 C35,28 19,46 19,46 Z" fill="none" stroke="#1d3b84" stroke-width="2.5" stroke-linejoin="round"/>
        <circle cx="19" cy="18" r="6.5" fill="none" stroke="#1d3b84" stroke-width="2.5"/>
      </svg>
      <p class="address">117 Parade Moana SA 5169</p>
      <div class="divider"></div>

      <p class="web">Menu &amp; Opening Hours<br>www.<b>saltreefcafe</b>.com.au</p>
    </div>
  </div>
</section>

</body>
</html>
```